Real estate website

Please find attached a rough outline of what we want for the design. This is just for placement to show what to have on the menu's as content, etc. but please make it look much more professional.
Please make the bottom footer a similar gradient to the logo
Please make the sign up now and log in buttons look better - these are just samples to show placement
Please use the correct logos for dwelloria.com.au, plotnex.com.au and roofquill.com.au
Where it has 'video embed' just leave that as is as we will replace that with a video.

```html
<!DOCTYPE html>
<html lang="en">
<head>
<meta charset="utf-8">
<title>Keyfold Direct – Sell With No Commission</title>
<link href="https://fonts.googleapis.com/css2?family=Inter:wght@400;500;600;700;800&display=swap" rel="stylesheet">
<style>
:root{
  --green-dark:#0f7a3a;
  --green:#2e9a3a;
  --green-light:#8cc832;
  --ink:#111111;
  --muted:#555555;
  --bg:#f6f6f6;
  --line:#cfd4d8;
  --red:#e60a0a;
  --white:#ffffff;
}
*{box-sizing:border-box;margin:0;padding:0}
html,body{width:1200px;height:711px;overflow:hidden}
body{font-family:"Inter",sans-serif;color:var(--ink);background:var(--bg);position:relative}
.site-header{position:absolute;left:0;top:0;width:1200px;height:102px;background:var(--white);box-shadow:0 2px 6px rgba(0,0,0,.04);z-index:3}
.brand{position:absolute;left:75px;top:30px;display:flex;align-items:center;gap:12px}
.brand-dot{width:40px;height:40px;border-radius:50%;background:linear-gradient(135deg,var(--green-dark),var(--green-light))}
.brand-name{font-size:34px;font-weight:400;color:var(--ink);letter-spacing:-.3px}
.main-nav a{position:absolute;top:48px;font-size:11.5px;color:var(--ink);text-decoration:none}
.btn-signup{position:absolute;left:947px;top:37px;width:106px;height:36px;border-radius:3px;background:linear-gradient(90deg,var(--green-dark),var(--green-light));color:var(--white);font-size:11.5px;font-weight:500;display:flex;align-items:center;justify-content:center}
.login{position:absolute;left:1076px;top:47px;display:flex;align-items:center;gap:5px;font-size:11.5px;color:#333}
.hero-deco{position:absolute;left:0;top:102px;z-index:0}
.hero-photo{position:absolute;left:-172px;top:142px;width:482px;height:482px;border-radius:50%;background:radial-gradient(circle at 55% 40%,#c9d6dc,#8fa3ad 60%,#5e6b72);overflow:hidden;z-index:1}
.play{position:absolute;left:85px;top:333px;width:80px;height:80px;border-radius:50%;background:rgba(255,255,255,.25);display:flex;align-items:center;justify-content:center;z-index:2}
.hero-title{position:absolute;left:391px;top:213px;font-size:31px;line-height:35px;font-weight:500;z-index:2}
.hero-title .accent{color:var(--green);font-weight:700}
.portals{position:absolute;left:396px;top:318px;list-style:none;z-index:2}
.portals li{display:flex;align-items:center;height:55px}
.portals li:nth-child(3){height:56px}
.portals .name{margin-left:26px;font-size:19px;font-weight:700;color:#222}
.guide{position:absolute;left:741px;top:150px;width:382px;z-index:2}
.guide h2{font-size:23.5px;font-weight:700;line-height:26px}
.guide .sub{font-size:14px;margin-top:6px}
.field{position:absolute;left:0;width:382px;height:40px;background:var(--white);border:1px solid var(--line);border-radius:3px;font-size:12px;padding-left:17px;display:flex;align-items:center}
.field .req{color:var(--red);margin-left:4px}
.field.active{border-color:var(--green)}
.field.active .label{position:absolute;left:10px;top:-8px;background:var(--bg);padding:0 5px;font-size:12px}
.field.active .value{font-size:10px;color:#666;margin-left:-1px;margin-top:-4px}
.field.active .caret{display:inline-block;width:1px;height:15px;background:var(--green);margin-left:6px;vertical-align:middle}
.robot{position:absolute;left:1px;top:263px;width:130px;height:32px;background:#f9f9f9;border:1px solid #d3d3d3;border-radius:2px;display:flex;align-items:center;padding-left:6px;font-size:5.5px;color:#222}
.robot .box{width:12px;height:12px;border:1px solid #c1c1c1;background:#fff;border-radius:2px;margin-right:6px}
.btn-submit{position:absolute;left:0;top:311px;width:83px;height:36px;border-radius:3px;background:linear-gradient(90deg,var(--green-dark),var(--green-light));color:var(--white);font-size:11.5px;font-weight:500;display:flex;align-items:center;justify-content:center;gap:6px}
.cta{position:absolute;left:382px;top:533px;font-size:27px;font-weight:400;z-index:2;white-space:nowrap}
.cta-phone{position:absolute;left:931px;top:531px;font-size:31px;font-weight:700;color:var(--red);z-index:2}
.intro{position:absolute;left:382px;top:582px;width:732px;font-size:9.4px;line-height:14.4px;color:#222;z-index:2}
.intro strong{font-weight:600}
.services{position:absolute;left:0;top:654px;width:1200px;height:57px;background:linear-gradient(90deg,var(--green-dark),var(--green) 40%,var(--green-light));display:flex;align-items:center;z-index:3}
.services span{position:absolute;color:var(--white);font-size:15px;font-weight:500}
.services i{position:absolute;top:17px;width:1px;height:22px;background:rgba(255,255,255,.85)}
</style>
</head>
<body>
<header class="site-header">
  <div class="brand"><span class="brand-dot"></span><span class="brand-name">Keyfold Direct</span></div>
  <nav class="main-nav">
    <a style="left:522px">Sell My Property</a>
    <a style="left:646px">Rent My Property</a>
    <a style="left:776px">Rental Management</a>
  </nav>
  <div class="btn-signup">Sign Up Now</div>
  <div class="login">
    <svg width="13" height="13" viewBox="0 0 13 13"><circle cx="5" cy="3.5" r="3" fill="#4aa33a"/><path d="M0 12c0-3 2.2-5 5-5s5 2 5 5z" fill="#4aa33a"/></svg>
    Login
  </div>
</header>

<svg class="hero-deco" width="1200" height="552" viewBox="0 0 1200 552">
  <polygon points="278,0 302,0 372,120 340,170" fill="#ececec"/>
  <polygon points="700,552 1200,180 1200,270 820,552" fill="#ffffff" opacity=".7"/>
  <circle cx="69" cy="281" r="266" fill="none" stroke="#e9e9e9" stroke-width="10"/>
</svg>

<div class="hero-photo" role="img" aria-label="Portrait of a smiling agent in a grey suit; video embed area"></div>
<div class="play"><svg width="26" height="26" viewBox="0 0 26 26"><polygon points="3,2 25,13 3,24 9,13" fill="#fff"/></svg></div>

<h1 class="hero-title">Sell With<br><span class="accent">No Commission</span> On</h1>

<ul class="portals">
  <li><svg width="18" height="18" viewBox="0 0 18 18"><polygon points="0,0 18,9 0,18 5,9" fill="#2e9a3a"/></svg><span class="name">dwelloria.com.au</span></li>
  <li><svg width="18" height="18" viewBox="0 0 18 18"><polygon points="0,0 18,9 0,18 5,9" fill="#2e9a3a"/></svg><span class="name">plotnex.com.au</span></li>
  <li><svg width="18" height="18" viewBox="0 0 18 18"><polygon points="0,0 18,9 0,18 5,9" fill="#2e9a3a"/></svg><span class="name">roofquill.com.au</span></li>
</ul>

<section class="guide">
  <h2>Get Your Free Guide</h2>
  <p class="sub">To Listing Privately In The ACT</p>
  <div class="field active" style="top:66px"><span class="label">Email<span class="req">*</span></span><span class="value">sam.porter@exa<span class="caret"></span></span></div>
  <div class="field" style="top:115px">First Name<span class="req">*</span></div>
  <div class="field" style="top:164px">Last Name<span class="req">*</span></div>
  <div class="field" style="top:213px">Phone Number<span class="req">*</span></div>
  <div class="robot"><span class="box"></span>I'm not a robot</div>
  <div class="btn-submit">Submit <svg width="9" height="9" viewBox="0 0 9 9"><polygon points="0,0 9,4.5 0,9 2.5,4.5" fill="#fff"/></svg></div>
</section>

<p class="cta">Want To Pay Nothing Upfront? Ask Us How</p>
<p class="cta-phone">0491570156</p>
<p class="intro">Listing A House In Australia For Sale Or Rental Is Costly! In The ACT, It's Even Worse! ACT Residents Are Paying More To List And Sell Online, Than In Other &nbsp;&nbsp;Parts Of Australia. <strong>Keyfold Direct Solves This Problem For You</strong>. Sell Or Rent Your Own Home Privately In The ACT With Keyfold Direct And Pay Zero Commission. &nbsp;&nbsp;You'll Be Listed For An Unlimited Time On All The Major Sites. All The Tools For Listing Are Inside Your Account, Sign Up Today And Get Started.</p>

<footer class="services">
  <span style="left:76px">Finance</span><i style="left:177px"></i>
  <span style="left:225px">Conveyancing</span><i style="left:370px"></i>
  <span style="left:417px">Building inspection</span><i style="left:595px"></i>
  <span style="left:642px">Pest Imspection</span><i style="left:800px"></i>
  <span style="left:847px">Valuation</span><i style="left:959px"></i>
  <span style="left:1006px">Market Appraisal</span>
</footer>
</body>
</html>
```